Construction company focused on concrete and shed construction.

We need to update our current business card for ridgeforgebuilds.com.au we would like an eye catching design with blue, grey and white incorporating our current logo.
Our company started off in concreting and due to varying factors we have expanded to include shed construction as well.
This has led to our current Logo looking a little out of place and somehow need to use the card to bring in the shed construction side of the business while not having to change current concrete look "KESTRO" logo as we already have this incorporated into our company clothing and are not willing to change this yet.
Photo image attached for inspiration/ visual reference of type of work, not to be used on final design.
Please no cheesy designs of men in hard hats and tools
Final design should demonstrate a modern and service focused company.

Target Market(s)

Farmers, Business owners, Developers, Architects, Commercial project delivery

Industry/Entity Type

Construction Company

Contact Information for Business Card

Kestro Constructions.
7b Harlow st
East Carrowbank Vale
03 62918873

Font styles to use
Other font styles liked:
• see font in logo

Colors
3176b5
b2b2b2

Requirements
Must have
• Easy to read font,
• good contrast between back ground and writing
Nice to have
• Modern and corporate look with a fun but professional image.
Should not have
• Comic images or shadow images of tools/ people.

```html
<!DOCTYPE html>
<html lang="en">
<head>
<meta charset="utf-8">
<title>Kestro Constructions – Business Card</title>
<link rel="stylesheet" href="https://fonts.googleapis.com/css2?family=Montserrat:wght@400;500;600&display=swap">
<style>
  :root {
    --brand-blue: #2f78b7;
    --brand-grey: #b2b2b2;
    --ink: #333a40;
    --paper: #ffffff;
    --backdrop: #e9ebee;
  }
  * { margin: 0; padding: 0; box-sizing: border-box; }
  html, body {
    width: 1200px; height: 852px; overflow: hidden;
    background: var(--backdrop);
    font-family: "Montserrat", Arial, sans-serif;
  }
  .sheet {
    width: 1200px; height: 852px;
    display: flex; flex-direction: column; align-items: center; justify-content: center;
    gap: 34px;
  }
  .card {
    position: relative;
    width: 660px; height: 377px;
    border-radius: 18px;
    overflow: hidden;
  }

  /* Front */
  .card--front { background: var(--brand-blue); }
  .emblem {
    position: absolute;
    display: flex; align-items: center; justify-content: center;
    border-radius: 50%;
    background: var(--brand-grey);
    border: 8px solid var(--paper);
    color: var(--paper);
    font-weight: 600;
    letter-spacing: 1px;
  }
  .card--front .emblem {
    width: 150px; height: 150px;
    left: 255px; top: 62px;
    font-size: 24px;
  }
  .front-title {
    position: absolute; left: 0; right: 0; top: 262px;
    text-align: center;
    color: var(--paper);
    font-size: 25px; font-weight: 500;
    letter-spacing: 2.5px;
  }

  /* Back */
  .card--back { background: var(--paper); }
  .side-band {
    position: absolute; left: 52px; top: 0; bottom: 0; width: 58px;
    background: var(--brand-blue);
  }
  .card--back .emblem {
    width: 96px; height: 96px;
    left: 33px; top: 30px;
    font-size: 15px;
    border-width: 6px;
  }
  .company {
    position: absolute; left: 150px; top: 56px;
    color: var(--brand-blue);
    font-size: 22px; font-weight: 500; letter-spacing: 2px;
  }
  .person {
    position: absolute; right: 42px; top: 118px;
    width: 230px;
    text-align: right;
    border-bottom: 1.5px solid var(--brand-blue);
    padding-bottom: 4px;
  }
  .person-name { color: var(--brand-blue); font-size: 25px; font-weight: 600; letter-spacing: 1px; }
  .person-role { color: var(--ink); font-size: 12px; margin-top: -2px; }
  .address {
    position: absolute; right: 42px; top: 196px;
    text-align: right; color: var(--ink);
    font-size: 13px; line-height: 1.45; font-style: normal;
  }
  .rule {
    position: absolute; left: 150px; right: 42px; top: 262px;
    height: 1.5px; background: var(--brand-blue);
  }
  .contacts {
    position: absolute; left: 150px; top: 276px;
    list-style: none; color: var(--ink);
    font-size: 14px; line-height: 1.55;
  }
  .contacts li { display: flex; align-items: center; gap: 8px; }
  .contacts svg { width: 11px; height: 11px; fill: none; stroke: var(--brand-blue); stroke-width: 1.6; }
  .contacts .phone-icon { fill: var(--brand-blue); stroke: none; }
  .accent { color: var(--brand-blue); }
</style>
</head>
<body>
<main class="sheet">
  <section class="card card--front" aria-label="Card front">
    <div class="emblem">KESTRO</div>
    <h1 class="front-title">KESTRO CONSTRUCTIONS.</h1>
  </section>

  <section class="card card--back" aria-label="Card back">
    <div class="side-band"></div>
    <div class="emblem">KESTRO</div>
    <h2 class="company">KESTRO CONSTRUCTIONS.</h2>

    <div class="person">
      <div class="person-name">Marcus Hale</div>
      <div class="person-role">Director</div>
    </div>

    <address class="address">
      7b Harlow st<br>East Carrowbank Vale
    </address>

    <div class="rule"></div>

    <ul class="contacts">
      <li>
        <svg viewBox="0 0 12 12" aria-hidden="true"><path class="phone-icon" d="M2.5 1l2 2-1 1.5c.7 1.4 1.8 2.5 3.2 3.2L8.2 6.7l2 2-1.2 1.8C5 10.3 1.7 7 1.5 3z"/></svg>
        03 62918873
      </li>
      <li>
        <svg viewBox="0 0 12 12" aria-hidden="true"><rect x="1" y="2.5" width="10" height="7"/><path d="M1 2.5l5 4 5-4"/></svg>
        info@kestrobuilds.com
      </li>
      <li>
        <svg viewBox="0 0 12 12" aria-hidden="true"><circle cx="6" cy="6" r="4.8"/><ellipse cx="6" cy="6" rx="2" ry="4.8"/><path d="M1.2 6h9.6"/></svg>
        <span>www.<span class="accent">kestrobuilds</span>.com</span>
      </li>
    </ul>
  </section>
</main>
</body>
</html>
```